Coral Ridge Networks Ltd

I need a website that is an informational only. We are a construction business building telecommunications sites. Seeing how our company is Coral Ridge the color blue might want to be incorporated in the color scheme.
I can provide more picture of towers and wireless communications if needed.
current website www.coralridgenet.ca

Industry/Entity Type

Wireless Telecommunications, Construction

Coding

Coded - Design and coding required

Number of Pages Required

2 page

Font styles to use
Sans Serif

Colors

Designer to choose colors to be used in the design.

```html
<!DOCTYPE html>
<html lang="en">
<head>
<meta charset="utf-8">
<title>Coral Ridge Networks Ltd</title>
<link href="https://fonts.googleapis.com/css2?family=Poppins:wght@400;500;600;700;800&display=swap" rel="stylesheet">
<style>
:root{
  --navy:#2c3d8c;
  --navy-dark:#1f2c6b;
  --sky:#2a9cc6;
  --sky-light:#6cc3e0;
  --ink:#151515;
  --text:#333;
  --white:#fff;
  --dark:#151a17;
  --footer:#2e3f8f;
  --bar:#1b2440;
}
*{margin:0;padding:0;box-sizing:border-box}
html,body{width:1200px;height:3617px;overflow:hidden;background:var(--white)}
body{position:relative;font-family:'Poppins',sans-serif;color:var(--text)}
a{color:inherit;text-decoration:none}

/* header */
.site-header{position:absolute;left:0;top:0;width:1200px;height:108px;background:var(--white)}
.brand{position:absolute;left:75px;top:28px;display:flex;align-items:center;gap:10px}
.brand-dot{width:22px;height:22px;border-radius:50%;background:var(--sky)}
.brand-name{font-size:30px;font-weight:500;color:var(--sky);letter-spacing:.5px}
.phone-pill{position:absolute;left:843px;top:3px;width:283px;height:50px;border-radius:25px;background:var(--navy);color:var(--white)}
.phone-pill svg{position:absolute;left:16px;top:10px}
.phone-label{position:absolute;left:71px;top:4px;font-size:14px;letter-spacing:4px;font-weight:500;line-height:16px}
.phone-number{position:absolute;left:71px;top:18px;font-size:23px;font-weight:700;letter-spacing:1px;line-height:28px}
.nav a{position:absolute;top:52px;height:56px;line-height:56px;font-size:16px;font-weight:600;color:var(--navy);white-space:nowrap}
.nav a.active{background:var(--navy);color:var(--white);text-align:center}

/* hero */
.hero{position:absolute;left:0;top:108px;width:1200px;height:590px;overflow:hidden}
.hero-photo{position:absolute;inset:0;background:
  radial-gradient(ellipse 260px 420px at 330px 260px,rgba(120,140,150,.55),rgba(120,140,150,0) 70%),
  linear-gradient(180deg,#1f8fbd 0%,#49aed3 45%,#8ccbe3 100%)}
.hero-curve{position:absolute;left:0;top:0}
.hero-title{position:absolute;left:603px;top:118px;font-size:53px;line-height:64px;font-weight:800;color:var(--white);text-shadow:2px 3px 3px rgba(0,0,0,.45);white-space:nowrap}
.hero-btn{position:absolute;left:719px;top:355px;width:263px;height:50px;border-radius:25px;background:var(--navy);color:var(--white);font-size:27px;font-weight:500;text-align:center;line-height:46px;border:2px solid #6f87d8;box-shadow:0 4px 6px rgba(0,0,0,.35)}
.hero-dots span{position:absolute;top:525px;width:23px;height:23px;background:var(--white)}
.hero-dots span.on{background:var(--navy)}

/* section titles */
.section-title{position:absolute;left:0;width:1200px;text-align:center;font-size:30px;font-weight:700;color:var(--ink)}
.intro{position:absolute;left:130px;top:826px;width:940px;text-align:center;font-size:15.5px;line-height:25px;color:var(--text)}

/* service cards */
.card-photo{position:absolute;top:949px;width:334px;height:449px;border-radius:6px;overflow:hidden}
.card-photo .frame{position:absolute;left:15px;top:15px;right:15px;bottom:15px;border:1.5px solid rgba(120,200,255,.8);border-radius:6px}
.card-title{position:absolute;top:1412px;width:334px;text-align:center;font-size:20px;font-weight:600;color:var(--navy)}
.card-text{position:absolute;top:1446px;width:334px;padding:0 12px;text-align:center;font-size:15px;line-height:25px;color:var(--text)}
.btn{position:absolute;height:41px;background:var(--navy);color:var(--white);font-size:15px;font-weight:500;text-align:center;line-height:41px;border-radius:4px;box-shadow:0 2px 4px rgba(0,0,0,.25)}

/* who we are */
.who-photo{position:absolute;left:0;top:1660px;width:601px;height:384px;background:
  radial-gradient(ellipse 90px 300px at 330px 230px,rgba(40,70,60,.55),rgba(40,70,60,0) 75%),
  linear-gradient(180deg,#a9c2dc 0%,#d6e1ec 45%,#eef2f6 70%,#f9fbfc 100%)}
.who-title{position:absolute;left:688px;top:1652px;font-size:30px;font-weight:700;color:var(--ink)}
.who-text{position:absolute;left:688px;top:1713px;width:448px;font-size:14.5px;line-height:25px;color:var(--text)}

/* projects */
.tile{position:absolute;border-radius:5px;overflow:hidden}
.tile-overlay{position:absolute;left:15px;top:14px;width:220px;height:188px;background:rgba(0,0,0,.72);text-align:center;color:var(--white)}
.tile-overlay h3{margin-top:52px;font-size:18px;font-weight:600}
.tile-overlay span{display:inline-block;margin-top:14px;width:112px;height:32px;line-height:30px;border:1.5px solid #d8b95a;font-size:13px}

/* contact */
.talk{position:absolute;left:0;top:2724px;width:1200px;height:506px;background:
  radial-gradient(ellipse 400px 200px at 900px 420px,rgba(60,75,55,.55),rgba(60,75,55,0) 70%),
  radial-gradient(ellipse at 60% 40%,#2a312c 0%,#151a17 70%)}
.talk-title{position:absolute;left:0;width:1200px;top:62px;text-align:center;font-size:34px;color:var(--white);font-weight:400}
.talk-title b{font-weight:700}
.talk-sub{position:absolute;left:0;width:1200px;text-align:center;color:var(--white);font-weight:500}
.field{position:absolute;border:1px solid #ddd;color:#eee;font-size:15px;padding:6px 9px;background:transparent}
.submit{position:absolute;left:616px;top:395px;width:185px;height:36px;background:var(--navy);color:var(--white);font-size:14px;font-weight:600;line-height:36px;padding-left:23px}
.submit svg{position:absolute;left:137px;top:11px}

/* partners */
.partner{position:absolute;top:3267px;width:75px;height:34px;border:1px solid #c9cfe6;background:var(--white)}
.partner i{position:absolute;left:10px;top:6px;width:55px;height:22px;border-radius:3px}
.partner i.round{left:26px;width:22px;border-radius:50%}

/* footer */
.footer{position:absolute;left:0;top:3340px;width:1200px;height:247px;background:var(--footer);color:var(--white)}
.footer-logo{position:absolute;left:75px;top:37px;width:172px;height:133px;background:var(--white);display:flex;align-items:center;justify-content:center;gap:8px}
.footer-logo .brand-dot{width:16px;height:16px}
.footer-logo span{font-size:22px;color:var(--sky);font-weight:500}
.social{position:absolute;top:190px;width:34px;height:34px;border-radius:50%;border:2px solid var(--white)}
.footer h4{position:absolute;top:30px;font-size:22px;font-weight:500;color:#cfd8ff;letter-spacing:.5px}
.footer-links a{position:absolute;left:523px;font-size:15px}
.info{position:absolute;left:958px;font-size:15px;line-height:25px}
.info-icon{position:absolute;left:932px}
.copyright{position:absolute;left:0;top:3587px;width:1200px;height:30px;background:var(--bar);color:var(--white);font-size:12px;text-align:center;line-height:30px}
</style>
</head>
<body>

<header class="site-header">
  <div class="brand"><span class="brand-dot"></span><span class="brand-name">coral ridge</span></div>
  <div class="phone-pill">
    <svg width="40" height="32" viewBox="0 0 40 32" fill="none" stroke="#fff" stroke-width="2.5"><path d="M8 4c-3 2-4 6-2 10 3 6 8 11 14 14 4 2 8 1 10-2l-5-5-4 3c-3-1-7-5-8-8l3-4z"/><path d="M22 4a10 10 0 0 1 10 10M22 9a5 5 0 0 1 5 5"/></svg>
    <div class="phone-label">CALL US</div>
    <div class="phone-number">1-604-555-0182</div>
  </div>
  <nav class="nav">
    <a class="active" style="left:327px;width:115px">HOME</a>
    <a style="left:474px">SERVICES</a>
    <a style="left:623px">ABOUT US</a>
    <a style="left:772px">COMPLETED PROJECTS</a>
    <a style="left:1017px">CONTACT US</a>
  </nav>
</header>

<section class="hero">
  <div class="hero-photo" role="img" aria-label="Technician working on a telecom tower against a blue sky"></div>
  <svg class="hero-curve" width="1200" height="590" viewBox="0 0 1200 590">
    <path d="M0 498 Q600 640 1200 498 L1200 590 L0 590Z" fill="#fff"/>
    <path d="M0 498 Q600 640 1200 498 Q600 610 0 498Z" fill="#2c3d8c"/>
  </svg>
  <h1 class="hero-title">WE SUPPLY AND<br>INSTALL ALL YOUR<br>TOWER NEEDS</h1>
  <a class="hero-btn">CONTACT US</a>
  <div class="hero-dots"><span class="on" style="left:528px"></span><span style="left:567px"></span><span style="left:606px"></span><span style="left:646px"></span></div>
</section>

<h2 class="section-title" style="top:762px">WHAT WE DO</h2>
<p class="intro">At Coral Ridge Networks Ltd Safety is number one.&nbsp; Coral Ridge is committed to a strong safety policy, protecting its staff and the general public from accidents and harm.&nbsp; All Coral Ridge Employees are certified “Tower Competent Climber and Rescue” from the Summit Safety Systems training program.</p>

<div class="card-photo" style="left:75px;background:linear-gradient(180deg,#2f6fc4 0%,#6fa3dc 30%,#e8eef4 48%,#6f7f70 62%,#5a6470 100%)" role="img" aria-label="Rooftop antenna site with mounts and equipment cabinets"><div class="frame"></div></div>
<div class="card-photo" style="left:432px;background:radial-gradient(ellipse 120px 260px at 170px 250px,rgba(200,200,190,.45),rgba(200,200,190,0) 70%),linear-gradient(180deg,#38598c 0%,#5e7fae 100%)" role="img" aria-label="Lattice telecom tower with dish antenna"><div class="frame"></div></div>
<div class="card-photo" style="left:790px;background:radial-gradient(ellipse 110px 90px at 210px 110px,rgba(220,60,40,.7),rgba(220,60,40,0) 70%),linear-gradient(135deg,#6a7078 0%,#c8703a 45%,#2a3a6a 100%)" role="img" aria-label="Technician connecting fibre cables in a server rack"><div class="frame"></div></div>

<h3 class="card-title" style="left:75px">ROOFTOP SITES</h3>
<h3 class="card-title" style="left:432px">TOWERS AND MONOPOLES</h3>
<h3 class="card-title" style="left:790px">IN BUILDING</h3>
<p class="card-text" style="left:75px">Structural upgrades or simple ballast mounts. Shelter on the ground, leasehold build outs...</p>
<p class="card-text" style="left:432px">Coral Ridge can engineer, supply and install all your tower needs.&nbsp; New structures or existing....</p>
<p class="card-text" style="left:790px">Small office or large Hotel.&nbsp; Coral Ridge has installed services into all size buildings....</p>
<a class="btn" style="left:156px;top:1544px;width:172px">LEARN MORE</a>
<a class="btn" style="left:513px;top:1544px;width:172px">LEARN MORE</a>
<a class="btn" style="left:871px;top:1544px;width:172px">LEARN MORE</a>

<div class="who-photo" role="img" aria-label="Snowy mountain landscape with a monopole tower"></div>
<h2 class="who-title">WHO WE ARE</h2>
<p class="who-text">At Coral Ridge Ltd, we are dedicated to providing our customers with friendly professional service. We value your business. We have made it our mission to provide reliable products and services in our customer-driven approach.</p>
<a class="btn" style="left:689px;top:1860px;width:173px">LEARN MORE</a>

<h2 class="section-title" style="top:2111px">COMPLETED PROJECTS</h2>

<div class="tile" style="left:75px;top:2201px;width:251px;height:216px;background:linear-gradient(135deg,#9a3a2e,#4c5a3a)" role="img" aria-label="Crew at a tower construction site">
  <div class="tile-overlay"><h3>PROJECT NAME</h3><span>VIEW DETAILS</span></div>
</div>
<div class="tile" style="left:75px;top:2432px;width:251px;height:216px;background:linear-gradient(180deg,#3a3f7a 0%,#c9565a 55%,#f0a070 100%)" role="img" aria-label="Tower silhouette at sunset"></div>
<div class="tile" style="left:341px;top:2201px;width:251px;height:447px;background:radial-gradient(ellipse 60px 200px at 125px 200px,rgba(230,235,240,.45),rgba(230,235,240,0) 75%),linear-gradient(180deg,#1563c8 0%,#3b8ae0 70%,#3f6a3a 100%)" role="img" aria-label="Tall lattice cell tower against blue sky"></div>
<div class="tile" style="left:608px;top:2201px;width:250px;height:216px;background:linear-gradient(180deg,#b9cbe0 0%,#dfe6ee 60%,#8b8f94 100%)" role="img" aria-label="Rooftop with microwave dishes"></div>
<div class="tile" style="left:608px;top:2432px;width:250px;height:216px;background:linear-gradient(180deg,#7aa0cc 0%,#c3d2e2 50%,#8f9399 100%)" role="img" aria-label="Rooftop antenna mounts with mountains behind"></div>
<div class="tile" style="left:873px;top:2201px;width:251px;height:283px;background:linear-gradient(180deg,#38598c,#5e7fae)" role="img" aria-label="Lattice tower top with dish"></div>
<div class="tile" style="left:873px;top:2500px;width:251px;height:148px;background:linear-gradient(180deg,#3d7fd0,#7b8a96)" role="img" aria-label="Rooftop site behind fencing"></div>

<section class="talk" role="img" aria-label="Dark forest backdrop behind contact form">
  <h2 class="talk-title">Let’s <b>Talk</b></h2>
  <p class="talk-sub" style="top:121px;font-size:17px">Have question or need help</p>
  <p class="talk-sub" style="top:146px;font-size:20px;font-weight:600">We would love to hear from you!</p>
  <div class="field" style="left:220px;top:225px;width:364px;height:36px">Name</div>
  <div class="field" style="left:220px;top:281px;width:364px;height:36px">E-mail</div>
  <div class="field" style="left:220px;top:338px;width:364px;height:37px">Tel</div>
  <div class="field" style="left:220px;top:395px;width:364px;height:36px">Company</div>
  <div class="field" style="left:616px;top:223px;width:364px;height:152px">Message</div>
  <a class="submit">GET STARTED<svg width="30" height="14" viewBox="0 0 30 14" fill="none" stroke="#fff" stroke-width="1.6"><path d="M0 7h28M22 1l6 6-6 6"/></svg></a>
</section>

<div class="partners" role="img" aria-label="Row of partner carrier badges">
  <div class="partner" style="left:90px"><i class="round" style="background:#d63a3a"></i></div>
  <div class="partner" style="left:168px"><i style="background:#2a63b8"></i></div>
  <div class="partner" style="left:247px"><i style="background:#7c4ba0"></i></div>
  <div class="partner" style="left:325px"><i class="round" style="background:#1f4ea3"></i></div>
  <div class="partner" style="left:404px"><i class="round" style="background:#d8202a"></i></div>
  <div class="partner" style="left:482px"><i style="background:#3a3a3a"></i></div>
  <div class="partner" style="left:561px"><i class="round" style="background:#1fa0df"></i></div>
  <div class="partner" style="left:639px"><i style="background:#222"></i></div>
  <div class="partner" style="left:718px"><i class="round" style="background:#e0187a"></i></div>
  <div class="partner" style="left:796px"><i style="background:#0d2a4f"></i></div>
  <div class="partner" style="left:875px"><i style="background:#2f58c8"></i></div>
  <div class="partner" style="left:953px"><i style="background:#f39a1c"></i></div>
  <div class="partner" style="left:1032px"><i style="background:#555"></i></div>
</div>

<footer class="footer">
  <div class="footer-logo"><span class="brand-dot"></span><span>coral ridge</span></div>
  <span class="social" style="left:76px"></span>
  <span class="social" style="left:144px"></span>
  <span class="social" style="left:212px"></span>
  <h4 style="left:524px">LINK</h4>
  <nav class="footer-links">
    <a style="top:74px">Home</a>
    <a style="top:104px">Services</a>
    <a style="top:135px">About Us</a>
    <a style="top:164px">Completed Projects</a>
    <a style="top:195px">Contact Us</a>
  </nav>
  <h4 style="left:932px">CONTACT INFO</h4>
  <svg class="info-icon" style="top:76px" width="16" height="24" viewBox="0 0 16 24"><path d="M8 0a8 8 0 0 0-8 8c0 6 8 16 8 16s8-10 8-16a8 8 0 0 0-8-8z" fill="#fff"/><circle cx="8" cy="8" r="3" fill="#2e3f8f"/></svg>
  <p class="info" style="top:74px">4471 Cedar Row<br>Fernvale, BC<br>V0X1K3</p>
  <svg class="info-icon" style="top:164px" width="20" height="20" viewBox="0 0 20 20" fill="none" stroke="#fff" stroke-width="1.6"><circle cx="10" cy="10" r="9"/><path d="M7 5c-2 1-2 3-1 5 1 2 3 4 5 5 2 1 3 0 4-1l-2-2-2 1c-1-1-2-2-3-3l1-2z"/></svg>
  <p class="info" style="top:160px">1-604-555-0182</p>
  <svg class="info-icon" style="top:205px" width="18" height="13" viewBox="0 0 18 13"><rect width="18" height="13" rx="1" fill="#fff"/><path d="M1 1l8 6 8-6" fill="none" stroke="#2e3f8f" stroke-width="1.5"/></svg>
  <p class="info" style="top:198px">info@coralridgenet.ca</p>
</footer>
<div class="copyright">Copyright 2022 Coral Ridge Ltd</div>

</body>
</html>
```